Business Card Design Project

I have just chosen a logo and would now like this designed onto a business card for my hair salon. I would like it to be classy not to busy and have a wow factor when people look at them
Has to Include on card:
Logo Design
And business details below
Kirra-mae Dunwell (owner)
0482 736 214
Vtk@lumbrex.com.au
18 Coralind Rise Merrow Flat
Logo is now attached please provide designs
Industry/Entity Type
Hair
Look and feel
Each slider illustrates characteristics of the customer's brand and the style your logo design should communicate.

```html
<!DOCTYPE html>
<html lang="en">
<head>
<meta charset="utf-8">
<title>Velour Hair Studio – Business Card</title>
<link rel="stylesheet" href="https://fonts.googleapis.com/css2?family=Roboto+Condensed:wght@700&display=swap">
<style>
  :root {
    --backdrop-light: #a3a493;
    --backdrop-dark: #8a8b7c;
    --card-rust: #a8462a;
    --band-copper-light: #c26d36;
    --band-copper-dark: #ad5229;
    --emblem-tan: #d08d46;
    --emblem-brown: #7a3520;
    --ink-white: #ffffff;
  }
  html, body {
    margin: 0;
    padding: 0;
    width: 1200px;
    height: 926px;
    overflow: hidden;
    background: radial-gradient(ellipse at 50% 40%, var(--backdrop-light) 0%, var(--backdrop-dark) 100%);
  }
  .canvas {
    position: relative;
    width: 1200px;
    height: 926px;
  }
  .business-card {
    position: absolute;
    left: 220px;
    top: 245px;
    width: 760px;
    height: 436px;
    background: var(--card-rust);
    overflow: hidden;
    box-shadow: 0 6px 18px rgba(0, 0, 0, 0.25);
  }
  .pattern-band {
    position: absolute;
    left: 0;
    top: 96px;
    width: 100%;
    height: 196px;
    background: linear-gradient(180deg, var(--band-copper-light) 0%, var(--band-copper-dark) 50%, var(--band-copper-light) 100%);
  }
  .emblem-area {
    position: absolute;
    left: 60px;
    top: 40px;
    width: 380px;
    height: 330px;
    background: radial-gradient(ellipse 52% 40% at 50% 50%,
      var(--emblem-tan) 0%, var(--emblem-tan) 78%,
      var(--emblem-brown) 84%, rgba(122, 53, 32, 0.35) 92%,
      rgba(122, 53, 32, 0) 100%);
  }
  .brand {
    position: absolute;
    left: 60px;
    top: 40px;
    width: 380px;
    height: 330px;
    display: flex;
    align-items: center;
    justify-content: center;
    gap: 14px;
  }
  .brand-mark {
    width: 16px;
    height: 16px;
    border-radius: 50%;
    background: var(--emblem-brown);
    flex: none;
  }
  .brand-name {
    margin: 0;
    font-family: "Roboto Condensed", sans-serif;
    font-weight: 700;
    color: var(--ink-white);
    line-height: 1;
    letter-spacing: 0.06em;
    text-align: center;
  }
  .brand-name .line-main {
    display: block;
    font-size: 52px;
  }
  .brand-name .line-sub {
    display: block;
    font-size: 27px;
    margin-top: 6px;
  }
  .contact-details {
    position: absolute;
    left: 420px;
    top: 128px;
    margin: 0;
    font-family: "Roboto Condensed", sans-serif;
    font-weight: 700;
    font-style: normal;
    font-size: 21px;
    line-height: 1.28;
    color: var(--ink-white);
    white-space: nowrap;
  }
  .contact-details .gap {
    display: block;
    height: 12px;
  }
</style>
</head>
<body>
<main class="canvas">
  <section class="business-card" aria-label="Velour Hair Studio business card">
    <div class="pattern-band" role="img" aria-label="Copper damask floral pattern band"></div>
    <div class="emblem-area" role="img" aria-label="Tan oval emblem framed by dark brown ornamental flourishes"></div>
    <div class="brand">
      <span class="brand-mark"></span>
      <h1 class="brand-name">
        <span class="line-main">VELOUR</span>
        <span class="line-sub">HAIR STUDIO</span>
      </h1>
    </div>
    <address class="contact-details">
      Kirra-mae Dunwell<br>
      + 0482 736 214
      <span class="gap"></span>
      Vtk@lumbrex.com.au<br>
      18 Coralind Rise Merrow Flat
    </address>
  </section>
</main>
</body>
</html>
```